Stationary for ultrasound imaging company
Business card, letter head, statonary envelope, fax cover sheet
Silver-Fern
Lino Varsek
Account Executive
20947 Marlow Pine Lane
Corvale, TX 75190
linovarsek@postmeadow.com
at www.brisolavent.com
This is the logo for the company.

```html
<!DOCTYPE html>
<html lang="en">
<head>
<meta charset="utf-8">
<title>Silver-Fern Business Card</title>
<link href="https://fonts.googleapis.com/css2?family=Open+Sans:wght@400;600;700&display=swap" rel="stylesheet">
<style>
  :root {
    --bg: #e9ebee;
    --blue: #3aa6de;
    --blue-deep: #1f86c4;
    --grey: #9c9fa3;
    --grey-light: #c9cbce;
    --text: #55585c;
    --white: #ffffff;
  }
  * { margin: 0; padding: 0; box-sizing: border-box; }
  html, body { width: 1200px; height: 864px; overflow: hidden; }
  body {
    background: var(--bg);
    font-family: "Open Sans", Arial, sans-serif;
    position: relative;
  }
  .card {
    position: absolute;
    width: 600px;
    height: 343px;
    border-radius: 18px;
    overflow: hidden;
    box-shadow: 0 10px 28px rgba(0,0,0,0.18);
  }
  /* Back */
  .card-back {
    left: 90px; top: 70px;
    background: var(--blue);
  }
  .back-mark {
    position: absolute;
    left: 0; right: 0; top: 112px;
    display: flex; align-items: center; justify-content: center; gap: 14px;
  }
  .back-mark .mark-square {
    width: 44px; height: 44px; background: var(--grey);
  }
  .back-mark .mark-name {
    color: var(--grey); font-weight: 700; font-size: 48px; letter-spacing: 0.5px;
  }
  .back-url {
    position: absolute; left: 0; right: 0; bottom: 60px;
    text-align: center; color: var(--white);
    font-size: 17px; letter-spacing: 3px;
  }
  /* Front */
  .card-front {
    left: 510px; top: 450px;
    background: var(--white);
  }
  .front-waves { position: absolute; left: 0; top: 0; width: 600px; height: 343px; }
  .brand {
    position: absolute; left: 34px; top: 52px;
    display: flex; align-items: center; gap: 12px;
  }
  .brand .mark-square { width: 42px; height: 42px; background: var(--blue); }
  .brand .brand-name {
    color: var(--blue-deep); font-weight: 700; font-size: 44px; line-height: 1;
  }
  .person {
    position: absolute; left: 60px; top: 132px;
    color: var(--text); font-size: 12.5px; line-height: 1.55;
  }
  .person .person-name { color: var(--blue-deep); font-weight: 700; font-size: 17px; }
  .person .person-title { margin-bottom: 8px; }
  .contacts {
    position: absolute; left: 330px; top: 128px;
    list-style: none; color: var(--text); font-size: 12.5px;
  }
  .contacts li { display: flex; align-items: center; gap: 8px; height: 20px; }
  .contact-icon { width: 15px; height: 15px; flex: none; }
</style>
</head>
<body>

  <section class="card card-back">
    <div class="back-mark">
      <span class="mark-square"></span>
      <span class="mark-name">Silver-Fern</span>
    </div>
    <p class="back-url">www.brisolavent.com</p>
  </section>

  <section class="card card-front">
    <svg class="front-waves" viewBox="0 0 600 343" aria-hidden="true">
      <path d="M0 312 C 180 326, 380 292, 600 264 L600 343 L0 343 Z" fill="var(--grey-light)"/>
      <path d="M0 324 C 190 334, 390 302, 600 282 L600 343 L0 343 Z" fill="var(--grey)"/>
      <path d="M0 334 C 200 340, 400 314, 600 298 L600 343 L0 343 Z" fill="var(--blue)"/>
    </svg>

    <div class="brand">
      <span class="mark-square"></span>
      <span class="brand-name">Silver-Fern</span>
    </div>

    <div class="person">
      <p class="person-name">Lino Varsek</p>
      <p class="person-title">Account Executive</p>
      <p>20947 Marlow Pine Lane</p>
      <p>Corvale, TX 75190</p>
    </div>

    <ul class="contacts">
      <li>
        <svg class="contact-icon" viewBox="0 0 16 16"><circle cx="8" cy="8" r="8" fill="var(--blue)"/><path d="M5 4.5l1.6-.4.9 2-1 .8a5 5 0 002.6 2.6l.8-1 2 .9-.4 1.6c-3.6.2-6.7-2.9-6.5-6.5z" fill="#fff"/></svg>
        <span>555-410-0142</span>
      </li>
      <li>
        <svg class="contact-icon" viewBox="0 0 16 16"><circle cx="8" cy="8" r="8" fill="var(--blue)"/><rect x="5" y="3.5" width="6" height="9" rx="1" fill="#fff"/><rect x="6" y="5" width="4" height="5" fill="var(--blue)"/></svg>
        <span>555-620-0187</span>
      </li>
      <li>
        <svg class="contact-icon" viewBox="0 0 16 16"><circle cx="8" cy="8" r="8" fill="var(--blue)"/><rect x="4" y="5" width="8" height="6" fill="#fff"/><rect x="5.5" y="3.5" width="5" height="2" fill="#fff"/></svg>
        <span>555-730-01946</span>
      </li>
      <li>
        <svg class="contact-icon" viewBox="0 0 16 16"><circle cx="8" cy="8" r="8" fill="var(--blue)"/><circle cx="8" cy="8" r="3" fill="#fff"/></svg>
        <span>linovarsek</span>
      </li>
      <li>
        <svg class="contact-icon" viewBox="0 0 16 16"><circle cx="8" cy="8" r="8" fill="var(--blue)"/><rect x="4" y="5" width="8" height="6" fill="#fff"/><path d="M4 5l4 3.5L12 5" stroke="var(--blue)" fill="none"/></svg>
        <span>linovarsek@postmeadow.com</span>
      </li>
      <li>
        <svg class="contact-icon" viewBox="0 0 16 16"><circle cx="8" cy="8" r="8" fill="var(--blue)"/><circle cx="8" cy="8" r="4" fill="none" stroke="#fff"/><path d="M4 8h8M8 4v8" stroke="#fff"/></svg>
        <span>www.brisolavent.com</span>
      </li>
    </ul>
  </section>

</body>
</html>
```